Redesign Digital Lending Mobile App - Android/ Flutter

Want to re-theme an existing Digital Lending Mobile app to simplify customer journeys, as well as uplift the UI.

Most users will have small screen phones so the design needs to take that into consideration while also adapting to those with larger devices, like admins with Tablets.

Have already laid out customer journeys on Figma with guidance on how the flow of the app should be. https://www.plandeck.example/board/q4tRw8KzPmYx2LbNvcHsaT/KovaPay?view-id=3-5120&k=Zu8pRtQwLmNcXbYa-2

Video capture of current app: https://vault.trelmora.example/clip/d/7Hq2WmRtLp9XzKcVbNa4YsDfGe8JuQo3/view
https://vault.trelmora.example/clip/d/4Pn8ZxCvBq1MwLtRyHs6KdJgFa2UeXi9/view

The documented views for Web are also here https://docs.quenlaro.example/open?id=3A8C2D4F6B1E9077!kb2d58e71403a4c6e8f2a91d04b7c3e68&resid=3A8C2D4F6B1E9077!kb2d58e71403a4c6e8f2a91d04b7c3e68&cid=3a8c2d4f6b1e9077&ithint=file%2Cdocx&redeem=bXhZc2RrcVp0TmxhUGVvV2lGcnVHc0JtWWpLdlFhWHpOcHRMZUR3U2JjUmZUeUFnSGxNb1ZpRXVKd0NrRHNYcVBuWmFNYmd5TGVr&migratedtospo=true&wdo=2
Updates

Target Market(s)

Kenya, Tanzania, Uganda - Africa

Industry/Entity Type

Fintech

Requirements
Must have
• Responsive for diff screens, esp. in context of smaller screen smartphone
Nice to have
• Thematic components to ensure new views can easily be adapted to these themse

```html
<!DOCTYPE html>
<html lang="en">
<head>
<meta charset="utf-8">
<title>KovaPay – Lending App Screens</title>
<link href="https://fonts.googleapis.com/css2?family=Open+Sans:wght@400;500;600;700&display=swap" rel="stylesheet">
<style>
:root{
  --stage:#2b7f86;
  --screen:#f4f4f5;
  --surface:#ffffff;
  --line:#e6e6e8;
  --ink:#2a2a2e;
  --muted:#6d6f75;
  --faint:#a3a5ab;
  --green:#3f9a5e;
  --green-soft:#e8f5ea;
  --blue:#1f5fbf;
  --blue-soft:#eaf2fd;
  --track:#e4e6ea;
}
*{box-sizing:border-box;margin:0;padding:0}
html,body{width:1200px;height:2805px;overflow:hidden}
body{background:var(--stage);font-family:"Open Sans",Arial,sans-serif;color:var(--ink);position:relative}
.screen{position:absolute;width:366px;height:795px;background:var(--screen);border-radius:38px;overflow:hidden}
.abs{position:absolute}
.status-bar{position:absolute;top:0;left:0;right:0;height:34px;font-size:12px;font-weight:600;padding:16px 0 0 20px}
.status-icons{position:absolute;right:18px;top:16px;display:flex;gap:6px}
.app-header{position:absolute;top:0;left:0;right:0;height:97px;background:var(--surface)}
.app-title{position:absolute;top:48px;left:0;right:0;text-align:center;font-size:17px;font-weight:500;letter-spacing:.3px}
.back{position:absolute;left:18px;top:52px}
.stat-row{display:flex;gap:6px}
.stat-card{width:79px;height:74px;background:var(--surface);border:1px solid var(--line);text-align:center;font-size:11px;color:var(--muted);padding-top:8px;line-height:1.55}
.stat-card b{display:block;font-weight:500;color:var(--ink);font-size:12px}
.section-title{font-size:15px;font-weight:500}
.filter-btn{width:78px;height:26px;background:var(--surface);border:1px solid var(--line);font-size:11px;color:var(--muted);display:flex;align-items:center;justify-content:center;gap:6px}
.status-item{left:18px;width:312px;height:40px}
.status-item .dot{position:absolute;left:0;top:4px;width:24px;height:24px;border-radius:50%;background:var(--surface);box-shadow:0 1px 3px rgba(0,0,0,.15);display:flex;align-items:center;justify-content:center}
.status-item .label{position:absolute;left:37px;top:0;font-size:13px}
.status-item .label span{font-weight:500;margin-left:4px}
.status-item .track{position:absolute;left:37px;top:24px;width:270px;height:3px;background:var(--track)}
.status-item .fill{height:3px}
.status-item .knob{position:absolute;top:-3px;width:9px;height:9px;border-radius:50%;background:#fff;border:1px solid #d6d8dc}
.blue{color:var(--blue)} .green{color:var(--green)}
.btn-next{width:80px;height:29px;background:var(--green);color:#fff;font-weight:600;font-size:15px;display:flex;align-items:center;justify-content:center;border-radius:2px}
.chart-box{background:var(--surface)}
.drawer{position:absolute;left:0;top:0;bottom:0;width:313px;background:var(--surface)}
.drawer-user{position:absolute;top:42px;left:20px;display:flex;gap:9px}
.avatar{width:31px;height:31px;border-radius:50%;background:var(--green);color:#fff;font-size:15px;display:flex;align-items:center;justify-content:center}
.user-name{font-size:11.5px;font-weight:500;line-height:1.3}
.user-meta{font-size:9px;color:var(--faint);line-height:1.25}
.menu-item{position:absolute;left:18px;display:flex;align-items:center;gap:9px;font-size:14.5px}
.table{position:absolute;left:17px;top:170px;width:332px}
.table-row{display:flex;gap:5px;margin-bottom:5px}
.table-row .k{width:164px;height:29px;font-size:12.5px;color:var(--muted);padding:5px 10px;border:1px solid #d5e4f7;background:var(--blue-soft)}
.table-row:nth-child(even) .k{background:var(--green-soft);border-color:#cfe8d4}
.table-row .v{flex:1;height:29px;font-size:12.5px;color:var(--muted);padding:5px 10px;background:var(--surface);border:1px solid var(--line)}
.filter-cat{position:absolute;left:0;width:185px;height:47px;font-size:14px;color:var(--muted);padding:14px 19px;border-bottom:1px solid var(--line)}
.filter-opt{position:absolute;left:203px;width:163px;font-size:14px;color:var(--muted);padding:14px 0 12px 26px;border-bottom:1px solid var(--line);line-height:1.3}
.filter-opt svg{position:absolute;left:0;top:18px}
.tab{height:24px;background:var(--surface);border:1px solid var(--line);font-size:10px;color:var(--muted);display:flex;align-items:center;justify-content:center}
.tab.on{background:#d9e7fa;border-color:#9dbce8;color:var(--blue)}
.toggle{height:29px;display:flex;align-items:center;justify-content:center;font-size:15px;font-weight:500}
</style>
</head>
<body>

<!-- Dashboard -->
<section class="screen" style="left:158px;top:130px" aria-label="Dashboard">
  <div class="app-header"></div>
  <div class="status-bar">9:41</div>
  <div class="status-icons"><svg width="40" height="10"><rect x="0" y="6" width="2" height="4"/><rect x="3" y="4" width="2" height="6"/><rect x="6" y="2" width="2" height="8"/><path d="M15 5a7 7 0 0 1 10 0l-5 5z"/><rect x="30" y="2" width="10" height="6" rx="1"/></svg></div>
  <svg class="abs" style="left:18px;top:50px" width="18" height="14"><g stroke="var(--blue)" stroke-width="2"><path d="M1 2h14M1 7h14M1 12h14"/></g></svg>
  <div class="app-title">DASHBOARD</div>

  <div class="stat-row abs" style="left:17px;top:114px">
    <div class="stat-card"><svg width="16" height="16"><circle cx="8" cy="8" r="6.5" fill="none" stroke="var(--blue)" stroke-width="1.4"/><text x="5" y="12" font-size="10" fill="var(--blue)">$</text></svg>Disbursed<b>$30k</b></div>
    <div class="stat-card"><svg width="20" height="16"><circle cx="10" cy="6" r="5" fill="none" stroke="var(--green)" stroke-width="1.4"/><path d="M2 15l4-5M18 15l-4-5" stroke="var(--green)" stroke-width="1.4"/></svg>Collected<b>$20k</b></div>
    <div class="stat-card"><svg width="18" height="16"><circle cx="8" cy="5" r="4" fill="none" stroke="var(--blue)" stroke-width="1.4"/><path d="M2 15a6 6 0 0 1 12 0z" fill="none" stroke="var(--blue)" stroke-width="1.4"/></svg>Active Clients<b>50</b></div>
    <div class="stat-card"><svg width="16" height="16"><path d="M8 1l2 5h5l-4 3 2 5-5-3-5 3 2-5-4-3h5z" fill="none" stroke="var(--green)" stroke-width="1.3"/></svg>New Clients<b>30</b></div>
  </div>

  <div class="section-title abs" style="left:18px;top:232px">Current Status</div>
  <div class="filter-btn abs" style="left:271px;top:228px"><svg width="12" height="10" stroke="var(--blue)"><path d="M0 2h12M0 5h12M0 8h12"/></svg>Filters</div>

  <div class="status-item abs" style="top:281px"><div class="dot"><svg width="12" height="12"><rect x="1" y="2" width="10" height="9" rx="1" fill="var(--blue)"/></svg></div><div class="label">Near Due: <span class="blue">$2.5M</span></div><div class="track"><div class="fill" style="width:135px;background:var(--blue)"></div><div class="knob" style="left:131px"></div></div></div>
  <div class="status-item abs" style="top:335px"><div class="dot"><svg width="12" height="12"><circle cx="6" cy="6" r="5" fill="var(--green)"/></svg></div><div class="label">Due: <span class="green">$35K</span></div><div class="track"><div class="fill" style="width:78px;background:var(--green)"></div><div class="knob" style="left:74px"></div></div></div>
  <div class="status-item abs" style="top:390px"><div class="dot"><svg width="12" height="12"><rect x="1" y="2" width="10" height="9" rx="1" fill="var(--blue)"/></svg></div><div class="label">Overdue: <span class="blue">$2.5M</span></div><div class="track"><div class="fill" style="width:135px;background:var(--blue)"></div><div class="knob" style="left:131px"></div></div></div>
  <div class="status-item abs" style="top:444px"><div class="dot"><svg width="12" height="12"><circle cx="6" cy="6" r="5" fill="var(--green)"/></svg></div><div class="label">Pending Disbursement&nbsp; : <span class="green">$35K</span></div><div class="track"><div class="fill" style="width:86px;background:var(--green)"></div><div class="knob" style="left:82px"></div></div></div>
  <div class="status-item abs" style="top:499px"><div class="dot"><svg width="12" height="12"><circle cx="6" cy="6" r="5" fill="var(--blue)"/><path d="M3.5 6l2 2 3-4" stroke="#fff" fill="none" stroke-width="1.3"/></svg></div><div class="label">Active Loans : <span class="blue">$2.5M</span></div><div class="track"><div class="fill" style="width:135px;background:var(--blue)"></div><div class="knob" style="left:131px"></div></div></div>

  <svg class="chart-box abs" style="left:47px;top:556px" width="272" height="127" viewBox="0 0 272 127">
    <defs><linearGradient id="dashFill" x1="0" y1="0" x2="0" y2="1"><stop offset="0" stop-color="#5b7ee6" stop-opacity=".75"/><stop offset="1" stop-color="#5b7ee6" stop-opacity=".05"/></linearGradient></defs>
    <path d="M22 102L49 56L79 40L109 62L158 64L196 49L232 64L252 102Z" fill="url(#dashFill)"/>
    <path d="M22 102L49 56L79 40L109 62L158 64L196 49L232 64L252 102" fill="none" stroke="var(--blue)" stroke-width="2"/>
    <g fill="#fff" stroke="var(--blue)" stroke-width="1.5"><circle cx="49" cy="56" r="3"/><circle cx="79" cy="40" r="3"/><circle cx="109" cy="62" r="3"/><circle cx="158" cy="64" r="3"/><circle cx="196" cy="49" r="3"/><circle cx="232" cy="64" r="3"/></g>
    <rect x="68" y="12" width="22" height="11" rx="2" fill="#e8e8ea"/><text x="72" y="20" font-size="7.5" fill="#333">448</text>
    <g font-size="6" fill="#999"><text x="20" y="118">01</text><text x="45" y="118">02</text><text x="70" y="118">03</text><text x="95" y="118">04</text><text x="120" y="118">05</text><text x="145" y="118">06</text><text x="170" y="118">07</text><text x="195" y="118">08</text><text x="220" y="118">09</text><text x="245" y="118">10</text></g>
  </svg>
  <div class="btn-next abs" style="left:144px;top:694px">Next</div>
</section>

<!-- Side menu -->
<section class="screen" style="left:673px;top:132px" aria-label="Navigation menu">
  <div class="abs" style="left:313px;top:0;right:0;height:97px;background:var(--surface)"></div>
  <div class="abs" style="left:330px;top:115px;width:40px;height:74px;background:var(--surface);border:1px solid var(--line)"></div>
  <div class="abs" style="left:326px;top:228px;font-size:15px;font-weight:500">Curre</div>
  <div class="abs" style="left:328px;top:281px;width:24px;height:24px;border-radius:50%;background:#fff;box-shadow:0 1px 3px rgba(0,0,0,.15)"></div>
  <div class="abs" style="left:328px;top:331px;width:24px;height:24px;border-radius:50%;background:#fff;box-shadow:0 1px 3px rgba(0,0,0,.15)"></div>
  <div class="abs" style="left:328px;top:385px;width:24px;height:24px;border-radius:50%;background:#fff;box-shadow:0 1px 3px rgba(0,0,0,.15)"></div>
  <div class="abs" style="left:328px;top:439px;width:24px;height:24px;border-radius:50%;background:#fff;box-shadow:0 1px 3px rgba(0,0,0,.15)"></div>
  <div class="abs" style="left:328px;top:493px;width:24px;height:24px;border-radius:50%;background:#fff;box-shadow:0 1px 3px rgba(0,0,0,.15)"></div>
  <svg class="abs" style="left:332px;top:50px" width="16" height="12"><g stroke="#333" stroke-width="1.6"><path d="M0 1h16M0 6h16M0 11h16"/></g></svg>

  <div class="drawer" style="box-shadow:2px 0 6px rgba(0,0,0,.08)">
    <div class="status-bar">9:41</div>
    <div class="drawer-user"><div class="avatar">S</div><div><div class="user-name">Amani Wekesa</div><div class="user-meta">Branch<br>Organizations</div></div></div>
    <div class="abs" style="left:0;right:0;top:97px;border-top:1px solid var(--line)"></div>
    <div class="menu-item" style="top:114px"><svg width="16" height="16" fill="none" stroke="#333" stroke-width="1.3"><rect x="1" y="1" width="6" height="6"/><rect x="9" y="1" width="6" height="9"/><rect x="1" y="9" width="6" height="6"/><rect x="9" y="12" width="6" height="3"/></svg>Dashboard</div>
    <div class="menu-item" style="top:150px"><svg width="16" height="16" fill="none" stroke="#333" stroke-width="1.3"><circle cx="8" cy="5" r="3.5"/><path d="M2 15a6 6 0 0 1 12 0"/></svg>Clients</div>
    <div class="menu-item" style="top:186px"><svg width="18" height="16" fill="none" stroke="#333" stroke-width="1.3"><circle cx="9" cy="5" r="2.5"/><circle cx="3.5" cy="7" r="2"/><circle cx="14.5" cy="7" r="2"/><path d="M4 15a5 5 0 0 1 10 0M0.5 14a3 3 0 0 1 3-3M17.5 14a3 3 0 0 0-3-3"/></svg>Groups</div>
    <div class="menu-item" style="top:222px"><svg width="16" height="16" fill="none" stroke="#333" stroke-width="1.3"><rect x="2" y="1" width="12" height="14"/><path d="M5 4h2M9 4h2M5 7h2M9 7h2M5 10h2M9 10h2M7 15v-3h2v3"/></svg>Centers</div>
    <div class="menu-item" style="top:257px"><svg width="16" height="16" fill="none" stroke="#333" stroke-width="1.3"><circle cx="8" cy="8" r="7"/><circle cx="8" cy="6.5" r="2.5"/><path d="M3.5 13a5 5 0 0 1 9 0"/></svg>Profile</div>
    <div class="abs" style="right:16px;top:726px;font-size:12px;color:var(--muted)">Version 1.0</div>
    <div class="abs" style="left:0;right:0;top:743px;border-top:1px solid var(--line)"></div>
    <div class="menu-item" style="top:758px"><svg width="17" height="16" fill="none" stroke="#333" stroke-width="1.3"><path d="M7 1H2v14h5M6 8h10M12 4l4 4-4 4"/></svg>Logout</div>
  </div>
</section>

<!-- Loan summary -->
<section class="screen" style="left:158px;top:1025px" aria-label="Loan summary">
  <div class="app-header"></div>
  <div class="status-bar">9:41</div>
  <div class="status-icons"><svg width="40" height="10"><rect x="0" y="6" width="2" height="4"/><rect x="3" y="4" width="2" height="6"/><rect x="6" y="2" width="2" height="8"/><path d="M15 5a7 7 0 0 1 10 0l-5 5z"/><rect x="30" y="2" width="10" height="6" rx="1"/></svg></div>
  <svg class="back" width="10" height="16"><path d="M8 2L2 8l6 6" fill="none" stroke="#333" stroke-width="1.8"/></svg>
  <div class="app-title">LOAN SUMMARY</div>
  <div class="section-title abs" style="left:17px;top:117px">Summary Details</div>
  <div class="filter-btn abs" style="left:270px;top:114px"><svg width="12" height="10" stroke="var(--blue)"><path d="M0 2h12M0 5h12M0 8h12"/></svg>Filters</div>
  <div class="table">
    <div class="table-row"><div class="k">Loan reference number</div><div class="v">3213</div></div>
    <div class="table-row"><div class="k">Loan status</div><div class="v">Active</div></div>
    <div class="table-row"><div class="k">Date disbursed</div><div class="v">13 July 2024</div></div>
    <div class="table-row"><div class="k">Date approved</div><div class="v">24 July 2024</div></div>
    <div class="table-row"><div class="k">Last repayment date</div><div class="v">13 October 2024</div></div>
    <div class="table-row"><div class="k">Next repayment date</div><div class="v">24 October 2024</div></div>
    <div class="table-row"><div class="k">Amount disbursed</div><div class="v">35,00,000</div></div>
    <div class="table-row"><div class="k">Amount outstanding</div><div class="v">35,00,000</div></div>
    <div class="table-row"><div class="k">Overdue days</div><div class="v">45</div></div>
  </div>
  <div class="btn-next abs" style="left:143px;top:535px">Next</div>
</section>

<!-- Filters -->
<section class="screen" style="left:673px;top:1025px;background:var(--surface)" aria-label="Filters">
  <div class="status-bar">9:41</div>
  <div class="abs" style="left:19px;top:46px;font-size:17px;color:#444">Filters</div>
  <div class="abs" style="left:0;right:0;top:89px;border-top:1px solid var(--line)"></div>
  <div class="abs" style="left:0;top:90px;width:185px;bottom:0;background:var(--screen)"></div>
  <div class="filter-cat" style="top:90px;background:var(--surface)">1.&nbsp;&nbsp; Loan status</div>
  <div class="filter-cat" style="top:137px">2.&nbsp;&nbsp; Loan officer</div>
  <div class="filter-cat" style="top:184px;background:var(--surface)">3.&nbsp;&nbsp; Branch</div>
  <div class="filter-cat" style="top:231px;background:var(--surface)">4.&nbsp;&nbsp; Fund</div>
  <div class="filter-cat" style="top:278px;background:var(--surface);border:none">5.&nbsp;&nbsp; Product</div>
  <div class="filter-opt" style="top:90px;color:var(--ink)"><svg width="12" height="10"><path d="M1 5l3.5 3.5L11 1" fill="none" stroke="var(--green)" stroke-width="1.6"/></svg>Active Loans</div>
  <div class="filter-opt" style="top:137px"><svg width="12" height="10"><path d="M1 5l3.5 3.5L11 1" fill="none" stroke="var(--faint)" stroke-width="1.3"/></svg>Near Due</div>
  <div class="filter-opt" style="top:184px"><svg width="12" height="10"><path d="M1 5l3.5 3.5L11 1" fill="none" stroke="var(--faint)" stroke-width="1.3"/></svg>Overdue</div>
  <div class="filter-opt" style="top:231px"><svg width="12" height="10"><path d="M1 5l3.5 3.5L11 1" fill="none" stroke="var(--faint)" stroke-width="1.3"/></svg>Pending<br>disbursement</div>
  <div class="filter-opt" style="top:297px;border:none"><svg width="12" height="10"><path d="M1 5l3.5 3.5L11 1" fill="none" stroke="var(--faint)" stroke-width="1.3"/></svg>Pending approval</div>
</section>

<!-- Report -->
<section class="screen" style="left:158px;top:1920px" aria-label="Report">
  <div class="app-header"></div>
  <div class="status-bar">9:41</div>
  <div class="status-icons"><svg width="40" height="10"><rect x="0" y="6" width="2" height="4"/><rect x="3" y="4" width="2" height="6"/><rect x="6" y="2" width="2" height="8"/><path d="M15 5a7 7 0 0 1 10 0l-5 5z"/><rect x="30" y="2" width="10" height="6" rx="1"/></svg></div>
  <svg class="back" width="10" height="16"><path d="M8 2L2 8l6 6" fill="none" stroke="#333" stroke-width="1.8"/></svg>
  <div class="app-title">REPORT</div>
  <div class="abs blue" style="left:0;right:0;top:111px;text-align:center;font-size:15px;font-weight:500">Total Loan</div>
  <div class="abs" style="left:77px;top:139px;width:213px;height:33px;background:var(--surface);border:1px solid var(--line);text-align:center;font-size:14px;padding-top:6px">$ 35,00,000</div>
  <div class="abs" style="left:0;right:0;top:196px;border-top:1px solid var(--line)"></div>
  <div class="section-title abs" style="left:18px;top:224px">Revenue report</div>
  <div class="filter-btn abs" style="left:271px;top:221px"><svg width="12" height="10" stroke="var(--blue)"><path d="M0 2h12M0 5h12M0 8h12"/></svg>Filters</div>
  <div class="toggle abs" style="left:19px;top:268px;width:80px;background:var(--green);color:#fff">Profit</div>
  <div class="toggle abs" style="left:104px;top:268px;width:80px;background:#d6ecdb;color:#555">Loss</div>
  <div class="tab abs" style="left:18px;top:330px;width:51px">Year</div>
  <div class="tab on abs" style="left:75px;top:330px;width:55px">Month</div>
  <div class="tab abs" style="left:134px;top:330px;width:51px">Week</div>
  <div class="tab abs" style="left:190px;top:330px;width:53px">Day</div>
  <svg class="abs" style="left:17px;top:365px" width="332" height="154" viewBox="0 0 332 154">
    <defs><linearGradient id="revFill" x1="0" y1="0" x2="0" y2="1"><stop offset="0" stop-color="#5b7ee6" stop-opacity=".45"/><stop offset="1" stop-color="#5b7ee6" stop-opacity="0"/></linearGradient></defs>
    <rect width="332" height="154" fill="#fff"/>
    <rect x="12" y="14" width="8" height="8" rx="1" fill="var(--blue)"/>
    <text x="24" y="21" font-size="8" fill="#444">June 2024</text>
    <path d="M20 97C50 80 80 92 110 92S170 80 200 64S250 95 270 94S300 82 310 80V125H20Z" fill="url(#revFill)"/>
    <path d="M20 97C50 80 80 92 110 92S170 80 200 64S250 95 270 94S300 82 310 80" fill="none" stroke="var(--blue)" stroke-width="2.5"/>
    <g font-size="8" fill="#666"><text x="12" y="136">Week 1</text><text x="106" y="136">Week 2</text><text x="200" y="136">Week 3</text><text x="295" y="136">Week 4</text></g>
  </svg>
  <div class="stat-row abs" style="left:17px;top:539px">
    <div class="stat-card"><svg width="20" height="18"><circle cx="10" cy="8" r="6.5" fill="none" stroke="var(--blue)" stroke-width="1.4"/><text x="7" y="12" font-size="10" fill="var(--blue)">$</text></svg>Revenue<b>$3000</b></div>
    <div class="stat-card"><svg width="20" height="18"><rect x="2" y="6" width="16" height="11" rx="1" fill="none" stroke="var(--green)" stroke-width="1.4"/><path d="M5 6l8-4 2 4" fill="none" stroke="var(--green)" stroke-width="1.4"/></svg>Expenses<b>$3000</b></div>
    <div class="stat-card"><svg width="18" height="18"><path d="M3 2h8l4 4v11H3z" fill="none" stroke="var(--blue)" stroke-width="1.4"/><path d="M6 14l6-6" stroke="var(--blue)" stroke-width="1.3"/></svg>Tax<b>$3000</b></div>
    <div class="stat-card"><svg width="24" height="18"><rect x="1" y="3" width="22" height="13" rx="2" fill="none" stroke="var(--green)" stroke-width="1.4"/><circle cx="12" cy="9.5" r="3" fill="none" stroke="var(--green)" stroke-width="1.3"/></svg>Salaries<b>$3000</b></div>
  </div>
</section>

</body>
</html>
```